" Nome da empresa: Recanto Vivale CLINICA DE NUTRIÇAO SOMOS NUTRICIONISTAS E DESEJAMOS PROPORCIONAR AOS NOSSOS PACIENTES UM TRATAMENTO INDIVIDUALIZADO. FAREMOS ATENDIMENTOS NUTRICIONAIS A FIM DE LEVAR QUALIDADE DE VIDA E PREVENÇAO de doenças, focando na educaçao nutricional "

```html
<!DOCTYPE html>
<html lang="pt-BR">
<head>
<meta charset="UTF-8">
<title>Recanto Vivale — Papel Timbrado</title>
<link href="https://fonts.googleapis.com/css2?family=Quicksand:wght@500;600&display=swap" rel="stylesheet">
<style>
  :root {
    --backdrop: #ecebe8;
    --paper: #ffffff;
    --teal: #1e5c57;
    --orange: #f08a24;
    --mark-grey: #d9d9d9;
    --footer-ink: #8a8f8e;
  }
  * { box-sizing: border-box; margin: 0; padding: 0; }
  html, body { width: 1200px; height: 1200px; overflow: hidden; }
  body {
    background: var(--backdrop);
    font-family: "Quicksand", sans-serif;
    position: relative;
  }
  .letterhead {
    position: absolute;
    top: 318px;
    width: 400px;
    height: 565px;
    background: var(--paper);
    box-shadow: 0 6px 18px rgba(0,0,0,0.12);
    overflow: hidden;
  }
  .letterhead--primary { left: 130px; }
  .letterhead--secondary { left: 670px; }

  .brand {
    position: absolute;
    top: 22px;
    left: 0;
    right: 0;
    display: flex;
    flex-direction: column;
    align-items: center;
    gap: 5px;
  }
  .brand__dot {
    width: 14px; height: 14px;
    border-radius: 50%;
    background: var(--orange);
  }
  .brand__name {
    font-size: 15px;
    font-weight: 600;
    color: var(--teal);
    letter-spacing: 0.2px;
  }

  .seal {
    position: absolute;
    border-radius: 50%;
    display: flex;
    align-items: center;
    justify-content: center;
    font-weight: 600;
  }
  .seal--faint {
    width: 190px; height: 190px;
    left: 105px; top: 160px;
    border: 3px solid var(--mark-grey);
    color: var(--mark-grey);
    font-size: 20px;
  }
  .seal--accent {
    width: 145px; height: 145px;
    right: 38px; top: 378px;
    border: 3px solid var(--orange);
    color: var(--orange);
    font-size: 16px;
  }

  .footer-line {
    position: absolute;
    left: 14px; right: 14px;
    bottom: 30px;
    font-size: 5px;
    color: var(--footer-ink);
    white-space: nowrap;
  }
  .letterhead--secondary .footer-line { left: 26px; }

  .base-band {
    position: absolute;
    left: 0; right: 0; bottom: 0;
    height: 9px;
    display: flex;
  }
  .base-band__orange { flex: 0 0 65%; background: var(--orange); }
  .base-band__teal { flex: 1; background: var(--teal); }

  .side-band {
    position: absolute;
    top: 0; bottom: 0; left: 0;
    width: 6px;
    background: var(--teal);
  }
</style>
</head>
<body>
  <section class="letterhead letterhead--primary">
    <header class="brand">
      <span class="brand__dot"></span>
      <span class="brand__name">Recanto Vivale</span>
    </header>
    <div class="seal seal--faint">Recanto Vivale</div>
    <p class="footer-line">Telefone (00) 0000-0000 | contato@recantovivale.com.br | Rua das Flores, 100 Centro Cidade Estado</p>
    <div class="base-band">
      <span class="base-band__orange"></span>
      <span class="base-band__teal"></span>
    </div>
  </section>

  <section class="letterhead letterhead--secondary">
    <span class="side-band"></span>
    <header class="brand">
      <span class="brand__dot"></span>
      <span class="brand__name">Recanto Vivale</span>
    </header>
    <div class="seal seal--accent">Recanto Vivale</div>
    <p class="footer-line">Telefone (00) 0000-0000 | contato@recantovivale.com.br | Rua das Flores, 100 Centro Cidade Estado</p>
  </section>
</body>
</html>
```